Car cleaning and lubrication automotive retail label

Designing a modern, trendy car cleaning and lubrication label for the retail automitive business. the label should be suitable for a retail home and garden product range. We are looking for a label that is realistic and colorful. Greens and blues are what we think would fit best for a eco label. We would like to stand out from other similar product ranges by design, meaning that we are looking for an ultra modern, simple, clean and professional design. We are also looking for a new design for the logo, clean and modern. It should include: The 'KALTOR' logo that can have any color and "Automotive".

Example text for cleaning product (please keep in mind we need a combi cleaning product label that is also suitable for a lubrication label)

The label should have a front and a back:
Front label: Texts and slogans (in dutch):
- Reiniger, ontvetter en polisher
- Bescherming en glans
- Veilig, geconcentreerd en eco friendly
- Milieuvriendelijk
Product name: Stainless Steel Cleaner
Image of car/stainless steel on car
Eco icon
+ Icons explaining the product (cleans stainless steel on car, protection and shine, safe and concentrated, eco friendly, cleaner, degreaser, polisher)

Back label:
Instructions to use
About the product
Remarks
Updates

Target Market(s)

Automotive, car cleaning, car lubrication, car additives

Industry/Entity Type

Automotive

Colors
0692cd
a64599
e33e95
acd037
f04a50
ec1f27
cadf82
33a6d7
33b8a4

Requirements
Must have
• Must have modern colors, cool look, attract customers by an original design

```html
<!DOCTYPE html>
<html lang="en">
<head>
<meta charset="utf-8">
<title>KALTOR Wash &amp; Wax – Stainless Steel Cleaner Label</title>
<link rel="stylesheet" href="https://fonts.googleapis.com/css2?family=Roboto:wght@400;700;900&family=Roboto+Condensed:wght@700;900&display=swap">
<style>
  :root {
    --page: #ffffff;
    --orange-deep: #ee6a1e;
    --orange-mid: #f5892a;
    --yellow: #fbb53c;
    --brand: #e4522a;
    --ink: #231f20;
    --swoosh: #e8531f;
    --eco-green: #1d5a2c;
    --eco-ring: #3aa845;
    --silver-light: #f4f4f4;
    --silver-mid: #c9c9c9;
    --silver-dark: #9a9a9a;
    --volume-text: #e8531f;
    --art-top: #f2894a;
    --art-bottom: #e0622c;
  }
  * { margin: 0; padding: 0; box-sizing: border-box; }
  html, body {
    width: 1200px; height: 1200px; overflow: hidden;
    background: var(--page);
    font-family: "Roboto", Arial, sans-serif;
  }
  .label {
    position: absolute; left: 289px; top: 199px;
    width: 595px; height: 793px; overflow: hidden;
    background: radial-gradient(ellipse at 50% 70%, var(--yellow) 0%, var(--orange-mid) 45%, var(--orange-deep) 100%);
  }
  .eco-badge {
    position: absolute; left: 221px; top: 5px; width: 154px; height: 154px;
    border-radius: 50%; background: var(--eco-green);
    border: 4px solid var(--eco-ring);
  }
  .brand-name {
    position: absolute; top: 168px; left: 0; width: 100%;
    text-align: center; font-family: "Roboto Condensed", Arial, sans-serif;
    font-weight: 900; font-size: 140px; line-height: 1;
    color: var(--brand);
  }
  .tagline {
    position: absolute; top: 172px; left: 0; width: 100%;
    text-align: center; font-size: 9px; font-weight: 700; color: var(--ink);
  }
  .product-line {
    position: absolute; top: 310px; left: 0; width: 100%; text-align: center;
    font-weight: 700; font-size: 45px; line-height: 1; color: var(--ink);
  }
  .product-line-es {
    position: absolute; top: 357px; left: 0; width: 100%; text-align: center;
    font-size: 15px; font-weight: 700; color: var(--ink);
  }
  .formula {
    position: absolute; left: 15px; top: 393px;
    font-size: 14px; font-weight: 700; color: var(--ink);
  }
  .formula-note {
    position: absolute; left: 15px; top: 414px;
    font-size: 9px; font-weight: 700; line-height: 1.35; color: var(--ink);
  }
  .car-art {
    position: absolute; left: 130px; top: 440px; width: 440px; height: 180px;
    border-radius: 14px;
    background: linear-gradient(180deg, var(--art-top), var(--art-bottom));
  }
  .band { position: absolute; left: 0; top: 0; width: 595px; height: 793px; }
  .volume {
    position: absolute; left: 40px; top: 488px; width: 136px; height: 136px;
    border-radius: 50%; background: #fff; border: 3px solid var(--silver-mid);
    display: flex; flex-direction: column; justify-content: center; align-items: center;
    font-weight: 700; font-size: 23px; line-height: 1.18;
    color: var(--volume-text); text-align: center; white-space: nowrap;
  }
  .product-name {
    position: absolute; top: 653px; left: 0; width: 100%; text-align: center;
    font-weight: 700; font-size: 45px; line-height: 42px; color: var(--ink);
  }
  .caution {
    position: absolute; top: 752px; left: 0; width: 100%; text-align: center;
    font-size: 9px; font-weight: 700; color: var(--ink);
  }
</style>
</head>
<body>
  <main class="label">
    <div class="eco-badge" role="img" aria-label="Eco friendly badge"></div>

    <h1 class="brand-name">KALTOR</h1>
    <p class="tagline">protection and shine, safe and concentrated, eco friendly, cleaner, degreaser, polisher</p>

    <h2 class="product-line">WASH &amp; WAX</h2>
    <p class="product-line-es">Lavado y encerado para automoviles</p>

    <p class="formula">Advanced Wash and Wax Formula</p>
    <p class="formula-note">Helps Water Beading &amp; Delivers<br>Incredible Glossmax Shine!</p>

    <div class="car-art" role="img" aria-label="Illustration of an orange sports car"></div>

    <svg class="band" viewBox="0 0 595 793" aria-hidden="true">
      <defs>
        <linearGradient id="silver" x1="0" y1="0" x2="0" y2="1">
          <stop offset="0" stop-color="#c9c9c9"/>
          <stop offset=".35" stop-color="#f4f4f4"/>
          <stop offset=".7" stop-color="#c9c9c9"/>
          <stop offset="1" stop-color="#9a9a9a"/>
        </linearGradient>
      </defs>
      <path d="M0 600 Q300 640 595 490 L595 793 L0 793 Z" fill="#e8531f"/>
      <path d="M0 626 Q300 650 595 510 L595 793 L0 793 Z" fill="url(#silver)"/>
    </svg>

    <div class="volume">
      <span>2 QT</span>
      <span>(64 FL OZ)</span>
      <span>1.89 L</span>
    </div>

    <h3 class="product-name">STAINLESS STEEL<br>CLEANER</h3>
    <p class="caution">CAUTION: EYE IRRITANT, READ CAUTIONS ON BACK LABEL</p>
  </main>
</body>
</html>
```